Kestramor Values/Culture for employees

Take our cultures list and create an on brand graphic that can be used for various media, ie. posters, screen savers etc. mykestramor.com
We're a medium sized company who installs permanent christmas lights primarily for homeowners. however we will do it for businesses as well. This graphic is going to be for our employees to help remind them the cultures and values we stand for to provide the best experience and products. Since Christmas lights are such an important part of our country's culture we want to make sure the internal culture of the company reflects that.

Target Market(s)

People who want to imrpove their home with permanent chrismas lights and never install them again

Requirements
Must have
• Proper styling with our brand colors and font (gotham)

Style guide is attached.

```html
<!DOCTYPE html>
<html lang="en">
<head>
<meta charset="utf-8">
<title>Kestramor – Our Cultural Beliefs</title>
<link href="https://fonts.googleapis.com/css2?family=Montserrat:wght@500;600;700&display=swap" rel="stylesheet">
<style>
  :root {
    --ink: #000000;
    --white: #ffffff;
    --green: #7ab52e;
    --frame: #3a3a3a;
    --glow-red: #7a1a2e;
    --glow-teal: #1e5f6a;
    --glow-violet: #5a1f6e;
    --glow-amber: #8a4a14;
    --night-top: #1c1470;
    --night-mid: #3a1a9a;
    --night-low: #7a2aa8;
    --rb-blue: #4a8fc8;
    --rb-yellow: #f6c431;
    --rb-orange: #f58a2a;
    --rb-red: #ee2a2a;
    --rb-pink: #e0397e;
    --rb-violet: #8a7aa8;
  }
  * { margin: 0; padding: 0; box-sizing: border-box; }
  html, body { width: 1200px; height: 928px; overflow: hidden; background: var(--ink); }
  .poster {
    position: relative;
    width: 1200px;
    height: 928px;
    background: var(--ink);
    border: 1px solid var(--frame);
    font-family: "Montserrat", sans-serif;
    color: var(--white);
    overflow: hidden;
  }
  .bokeh-field {
    position: absolute;
    left: 0; top: 0;
    width: 411px; height: 928px;
    background:
      radial-gradient(circle at 30% 10%, var(--glow-red) 0, transparent 28%),
      radial-gradient(circle at 70% 25%, var(--glow-violet) 0, transparent 30%),
      radial-gradient(circle at 15% 45%, var(--glow-violet) 0, transparent 25%),
      radial-gradient(circle at 60% 55%, var(--glow-teal) 0, transparent 26%),
      radial-gradient(circle at 20% 62%, var(--glow-amber) 0, transparent 20%),
      radial-gradient(circle at 55% 80%, var(--glow-violet) 0, transparent 28%),
      radial-gradient(circle at 25% 92%, var(--glow-teal) 0, transparent 22%),
      linear-gradient(90deg, rgba(0,0,0,0) 60%, var(--ink) 100%);
    opacity: 0.85;
  }
  .beliefs {
    position: absolute;
    left: 73px;
    top: 58px;
    width: 600px;
  }
  .beliefs-title {
    font-size: 52px;
    font-weight: 700;
    line-height: 1;
    letter-spacing: 0.5px;
    margin-bottom: 20px;
  }
  .belief { margin-bottom: 0; }
  .belief-name {
    color: var(--green);
    font-size: 20.5px;
    font-weight: 600;
    line-height: 36px;
    letter-spacing: 0.4px;
  }
  .belief-text {
    font-size: 19.5px;
    font-weight: 700;
    line-height: 39.5px;
    letter-spacing: 0.5px;
  }
  .brand-name {
    position: absolute;
    left: 716px;
    top: 285px;
    width: 420px;
    text-align: center;
    font-size: 42px;
    font-weight: 600;
    letter-spacing: 12px;
    line-height: 1;
    color: var(--white);
  }
  .brand-dot {
    position: absolute;
    left: 908px;
    top: 145px;
    width: 40px;
    height: 40px;
    border-radius: 50%;
    background: var(--green);
  }
  .home-photo {
    position: absolute;
    left: 716px;
    top: 349px;
    width: 420px;
    height: 506px;
    background:
      radial-gradient(ellipse at 60% 45%, rgba(230,80,220,0.45) 0, transparent 50%),
      linear-gradient(180deg, var(--night-top) 0%, var(--night-mid) 45%, var(--night-low) 100%);
  }
  .rainbow-rule {
    position: absolute;
    left: 0;
    top: 881px;
    width: 1200px;
    height: 6px;
    background: linear-gradient(90deg, var(--rb-blue) 0%, var(--rb-yellow) 25%, var(--rb-orange) 38%, var(--rb-red) 55%, var(--rb-pink) 78%, var(--rb-violet) 100%);
  }
</style>
</head>
<body>
<div class="poster">
  <div class="bokeh-field" role="img" aria-label="Soft out-of-focus bokeh of colourful holiday lights"></div>

  <section class="beliefs">
    <h1 class="beliefs-title">Our Cultural Beliefs</h1>
    <div class="belief">
      <h2 class="belief-name">Customer First</h2>
      <p class="belief-text">I strive to meet our customer’s needs and deliver<br>exceptional experiences.</p>
    </div>
    <div class="belief">
      <h2 class="belief-name">Own It</h2>
      <p class="belief-text">I demonstrate commitment by showing up “all in,” all<br>the time, even when it requires sacrifice.</p>
    </div>
    <div class="belief">
      <h2 class="belief-name">Simplify</h2>
      <p class="belief-text">I eliminate complexity and solve problems for<br>sustainable results.</p>
    </div>
    <div class="belief">
      <h2 class="belief-name">Build Trust</h2>
      <p class="belief-text">I trust people to do their best, let them perform and<br>then coach them to perform at even higher levels.</p>
    </div>
    <div class="belief">
      <h2 class="belief-name">Seize The Day</h2>
      <p class="belief-text">I am a big part of something big. What I do today will<br>help us win together!</p>
    </div>
    <div class="belief">
      <h2 class="belief-name">Do It Now</h2>
      <p class="belief-text">I work above the line, continue to ask “What else can I<br>do to deliver results?” and refuse to blame others.</p>
    </div>
  </section>

  <div class="brand-dot"></div>
  <div class="brand-name">KESTRAMOR</div>

  <div class="home-photo" role="img" aria-label="Two-storey house at night outlined with permanent colourful roofline lights"></div>

  <div class="rainbow-rule"></div>
</div>
</body>
</html>
```